Gently Harbor BC 2019

Hi!
As seen from the attached, I created a 2018 BC that I really like.
It features company details on one side, and a calendar on the other side. The BC is 7" x 2" with a score, so folded it's a regular sized BC.
Company details remain the same, but I need to upgrade and refresh the calendar to 2019. Let your creative juices flow!

The submitted designs so far, while not terrible, most don't take into account that I need a refresher on the current design, but it's a BC that is double sided, and the size of a BC that's side by side wide, with score. (see the attached BC 2018 design). I need the BC to be updated with a 2019 calendar, but essentially because it's such a tiny size, to work the realistic space allocated, and make it readable and striking to stand out and very usable/practical. Let's do this people!

```html
<!DOCTYPE html>
<html lang="en">
<head>
<meta charset="utf-8">
<title>Gently Harbor – Business Card 2019</title>
<link rel="stylesheet" href="https://fonts.googleapis.com/css2?family=Lato:wght@400;700&family=Montserrat:wght@600;700&family=Courier+Prime&display=swap">
<style>
  :root{
    --stage:#2e2e2e;
    --card:#ffffff;
    --ink:#1e1e1e;
    --panel-dark:#161616;
    --panel-mid:#222222;
    --band-grey:#e4e4e6;
    --rule:#d6d6d8;
    --cyan:#1aa9e1;
    --magenta:#e2198a;
    --yellow:#fff200;
    --green:#3bb34a;
    --fax-blue:#2f8fd8;
    --month-blue:#2a8ccf;
    --sunday:#e2344b;
    --stripe-green:#63bd8a;
    --stripe-orange:#f39a1e;
    --stripe-purple:#8d3b8f;
    --stripe-coral:#e9546b;
    --stripe-yellow:#f7b71c;
  }
  *{margin:0;padding:0;box-sizing:border-box}
  html,body{width:1200px;height:755px;overflow:hidden;background:var(--stage)}
  .stage{position:relative;width:1200px;height:755px}

  .card{position:absolute;top:218px;width:498px;height:286px;background:var(--card);overflow:hidden}
  .card--details{left:90px}
  .card--calendar{left:620px;width:496px}

  /* details side */
  .details-shapes{position:absolute;inset:0}
  .taglines{position:absolute;left:16px;top:168px;list-style:none}
  .tagline{width:211px;height:15px;border-radius:8px;margin-bottom:10px;
    font:10.5px/15px "Courier Prime",monospace;color:var(--ink);padding-left:11px;white-space:nowrap}
  .tagline--cyan{background:var(--cyan)}
  .tagline--magenta{background:var(--magenta)}
  .tagline--yellow{background:var(--yellow)}

  .brand{position:absolute;left:300px;top:94px;display:flex;align-items:center;gap:8px;
    font:700 20px/1 "Lato",sans-serif;color:var(--ink);white-space:nowrap}
  .brand-mark{width:14px;height:14px;background:var(--magenta)}

  .contact-row{position:absolute;left:237px;right:0;display:flex;align-items:center;
    font:400 13px/1 "Lato",sans-serif;color:var(--ink);white-space:nowrap}
  .contact-row::after{content:"";position:absolute;left:46px;right:0;bottom:0;height:1px;background:var(--rule)}
  .contact-row--lines::after{display:none}
  .contact-icon{flex:none;width:46px;height:100%;display:flex;align-items:center;justify-content:center}
  .contact-row--phone{top:130px;height:36px}
  .contact-row--web{top:166px;height:38px}
  .contact-row--mail{top:204px;height:39px}
  .contact-row--lines{top:243px;height:43px}
  .contact-row--phone .contact-icon{background:var(--cyan)}
  .contact-row--web .contact-icon{background:var(--yellow)}
  .contact-row--mail .contact-icon{background:var(--magenta)}
  .contact-row--phone .contact-text{margin-left:8px}
  .contact-row--web .contact-text{margin-left:16px}
  .contact-row--mail .contact-text{margin-left:20px}
  .contact-row--lines .contact-text{margin-left:24px}
  .chat-dot{width:13px;height:13px;border-radius:50%;background:var(--green)}
  .fax-icon{margin:0 5px 0 10px}

  /* calendar side */
  .calendar-strip{position:absolute;left:0;top:0;width:76px;height:286px}
  .months{position:absolute;left:88px;top:30px;display:grid;
    grid-template-columns:repeat(4,84px);column-gap:14px;row-gap:8px}
  .month{height:74px}
  .month-name{font:700 8px/1 "Montserrat",sans-serif;color:var(--month-blue);
    text-align:center;letter-spacing:.4px;margin-bottom:3px}
  .weekdays,.days{display:grid;grid-template-columns:repeat(7,12px);
    font:700 6.4px/8px "Montserrat",sans-serif;color:var(--ink);text-align:center}
  .weekdays{border-bottom:1px solid var(--ink);margin-bottom:1px}
  .weekdays span:first-child,.days > :nth-child(7n+1){color:var(--sunday)}
</style>
</head>
<body>
<div class="stage">

  <!-- Details side -->
  <section class="card card--details" aria-label="Business card, contact side">
    <svg class="details-shapes" width="498" height="286" viewBox="0 0 498 286">
      <defs>
        <linearGradient id="panelShade" x1="0" y1="0" x2="1" y2="1">
          <stop offset="0" stop-color="var(--panel-mid)"/>
          <stop offset="1" stop-color="var(--panel-dark)"/>
        </linearGradient>
      </defs>
      <polygon points="216,0 258,0 298,286 240,286" fill="var(--band-grey)"/>
      <polygon points="0,0 216,0 240,286 0,286" fill="url(#panelShade)" role="img" aria-label="Dark panel with fine woven plaid texture"/>
    </svg>

    <ul class="taglines">
      <li class="tagline tagline--cyan">Fill your toner with purpose</li>
      <li class="tagline tagline--magenta">Fill your planet with hope</li>
      <li class="tagline tagline--yellow">Fill your world with kindness</li>
    </ul>

    <div class="brand"><span class="brand-mark"></span>Gently Harbor</div>

    <div class="contact-row contact-row--phone">
      <span class="contact-icon">
        <svg width="14" height="11" viewBox="0 0 14 11"><path d="M1 4c0-2 2-3 6-3s6 1 6 3l-3 1-1-2H5L4 5zM3 6h8l1 4H2z" fill="#fff"/></svg>
      </span>
      <span class="contact-text">555.310.4821</span>
    </div>
    <div class="contact-row contact-row--web">
      <span class="contact-icon">
        <svg width="13" height="10" viewBox="0 0 13 10"><rect x=".5" y=".5" width="12" height="9" fill="#fff"/><path d="M.5 .5l6 5 6-5" fill="none" stroke="var(--yellow)" stroke-width="1"/></svg>
      </span>
      <span class="contact-text">gentlyharbor.com</span>
    </div>
    <div class="contact-row contact-row--mail">
      <span class="contact-icon">
        <svg width="14" height="14" viewBox="0 0 14 14" fill="none" stroke="#fff" stroke-width="1.3"><circle cx="7" cy="7" r="6"/><ellipse cx="7" cy="7" rx="2.6" ry="6"/><path d="M1 7h12M2 3.8h10M2 10.2h10"/></svg>
      </span>
      <span class="contact-text">pickup@gentlyharbor.com</span>
    </div>
    <div class="contact-row contact-row--lines">
      <span class="contact-icon"><span class="chat-dot"></span></span>
      <span class="contact-text">555.310.4822</span>
      <svg class="fax-icon" width="14" height="12" viewBox="0 0 14 12"><rect x="3" y="0" width="8" height="4" fill="var(--fax-blue)"/><rect x="0" y="3" width="14" height="6" rx="1.5" fill="var(--fax-blue)"/><rect x="3" y="7" width="8" height="5" fill="#fff" stroke="var(--fax-blue)"/></svg>
      <span>555.720.3369</span>
    </div>
  </section>

  <!-- Calendar side -->
  <section class="card card--calendar" aria-label="Business card, 2019 calendar side">
    <svg class="calendar-strip" width="76" height="286" viewBox="0 0 76 286">
      <polygon points="0,0 76,0 76,8 0,34" fill="var(--stripe-green)"/>
      <polygon points="0,34 76,8 76,48 0,74" fill="var(--stripe-orange)"/>
      <polygon points="0,74 76,48 76,92 0,118" fill="var(--stripe-purple)"/>
      <polygon points="0,118 76,92 76,140 0,166" fill="var(--stripe-coral)"/>
      <polygon points="0,166 76,140 76,186 0,212" fill="var(--stripe-yellow)"/>
      <polygon points="0,212 76,186 76,232 0,258" fill="var(--stripe-purple)"/>
      <polygon points="0,258 76,232 76,286 0,286" fill="var(--stripe-green)"/>
      <g fill="#fff">
        <text transform="translate(22 192) rotate(-90)" font-family="Montserrat, sans-serif" font-weight="600" font-size="9" letter-spacing="5">CALENDAR</text>
        <text transform="translate(58 232) rotate(-90)" font-family="Montserrat, sans-serif" font-weight="600" font-size="32" letter-spacing="5">2019</text>
      </g>
      <g stroke="#fff" stroke-width="1.2">
        <line x1="14" y1="48" x2="14" y2="84"/>
        <line x1="14" y1="204" x2="14" y2="240"/>
        <line x1="64" y1="98" x2="64" y2="104"/>
      </g>
    </svg>

    <div class="months">
      <div class="month"><p class="month-name">JANUARY</p>
        <div class="weekdays"><span>S</span><span>M</span><span>T</span><span>W</span><span>T</span><span>F</span><span>S</span></div>
        <div class="days"><i></i><i></i><span>1</span><span>2</span><span>3</span><span>4</span><span>5</span><span>6</span><span>7</span><span>8</span><span>9</span><span>10</span><span>11</span><span>12</span><span>13</span><span>14</span><span>15</span><span>16</span><span>17</span><span>18</span><span>19</span><span>20</span><span>21</span><span>22</span><span>23</span><span>24</span><span>25</span><span>26</span><span>27</span><span>28</span><span>29</span><span>30</span><span>31</span></div></div>
      <div class="month"><p class="month-name">FEBRUARY</p>
        <div class="weekdays"><span>S</span><span>M</span><span>T</span><span>W</span><span>T</span><span>F</span><span>S</span></div>
        <div class="days"><i></i><i></i><i></i><i></i><i></i><span>1</span><span>2</span><span>3</span><span>4</span><span>5</span><span>6</span><span>7</span><span>8</span><span>9</span><span>10</span><span>11</span><span>12</span><span>13</span><span>14</span><span>15</span><span>16</span><span>17</span><span>18</span><span>19</span><span>20</span><span>21</span><span>22</span><span>23</span><span>24</span><span>25</span><span>26</span><span>27</span><span>28</span></div></div>
      <div class="month"><p class="month-name">MARCH</p>
        <div class="weekdays"><span>S</span><span>M</span><span>T</span><span>W</span><span>T</span><span>F</span><span>S</span></div>
        <div class="days"><i></i><i></i><i></i><i></i><i></i><span>1</span><span>2</span><span>3</span><span>4</span><span>5</span><span>6</span><span>7</span><span>8</span><span>9</span><span>10</span><span>11</span><span>12</span><span>13</span><span>14</span><span>15</span><span>16</span><span>17</span><span>18</span><span>19</span><span>20</span><span>21</span><span>22</span><span>23</span><span>24</span><span>25</span><span>26</span><span>27</span><span>28</span><span>29</span><span>30</span><span>31</span></div></div>
      <div class="month"><p class="month-name">APRIL</p>
        <div class="weekdays"><span>S</span><span>M</span><span>T</span><span>W</span><span>T</span><span>F</span><span>S</span></div>
        <div class="days"><i></i><span>1</span><span>2</span><span>3</span><span>4</span><span>5</span><span>6</span><span>7</span><span>8</span><span>9</span><span>10</span><span>11</span><span>12</span><span>13</span><span>14</span><span>15</span><span>16</span><span>17</span><span>18</span><span>19</span><span>20</span><span>21</span><span>22</span><span>23</span><span>24</span><span>25</span><span>26</span><span>27</span><span>28</span><span>29</span><span>30</span></div></div>
      <div class="month"><p class="month-name">MAY</p>
        <div class="weekdays"><span>S</span><span>M</span><span>T</span><span>W</span><span>T</span><span>F</span><span>S</span></div>
        <div class="days"><i></i><i></i><i></i><span>1</span><span>2</span><span>3</span><span>4</span><span>5</span><span>6</span><span>7</span><span>8</span><span>9</span><span>10</span><span>11</span><span>12</span><span>13</span><span>14</span><span>15</span><span>16</span><span>17</span><span>18</span><span>19</span><span>20</span><span>21</span><span>22</span><span>23</span><span>24</span><span>25</span><span>26</span><span>27</span><span>28</span><span>29</span><span>30</span><span>31</span></div></div>
      <div class="month"><p class="month-name">JUNE</p>
        <div class="weekdays"><span>S</span><span>M</span><span>T</span><span>W</span><span>T</span><span>F</span><span>S</span></div>
        <div class="days"><i></i><i></i><i></i><i></i><i></i><i></i><span>1</span><span>2</span><span>3</span><span>4</span><span>5</span><span>6</span><span>7</span><span>8</span><span>9</span><span>10</span><span>11</span><span>12</span><span>13</span><span>14</span><span>15</span><span>16</span><span>17</span><span>18</span><span>19</span><span>20</span><span>21</span><span>22</span><span>23</span><span>24</span><span>25</span><span>26</span><span>27</span><span>28</span><span>29</span><span>30</span></div></div>
      <div class="month"><p class="month-name">JULY</p>
        <div class="weekdays"><span>S</span><span>M</span><span>T</span><span>W</span><span>T</span><span>F</span><span>S</span></div>
        <div class="days"><i></i><span>1</span><span>2</span><span>3</span><span>4</span><span>5</span><span>6</span><span>7</span><span>8</span><span>9</span><span>10</span><span>11</span><span>12</span><span>13</span><span>14</span><span>15</span><span>16</span><span>17</span><span>18</span><span>19</span><span>20</span><span>21</span><span>22</span><span>23</span><span>24</span><span>25</span><span>26</span><span>27</span><span>28</span><span>29</span><span>30</span><span>31</span></div></div>
      <div class="month"><p class="month-name">AUGUST</p>
        <div class="weekdays"><span>S</span><span>M</span><span>T</span><span>W</span><span>T</span><span>F</span><span>S</span></div>
        <div class="days"><i></i><i></i><i></i><i></i><span>1</span><span>2</span><span>3</span><span>4</span><span>5</span><span>6</span><span>7</span><span>8</span><span>9</span><span>10</span><span>11</span><span>12</span><span>13</span><span>14</span><span>15</span><span>16</span><span>17</span><span>18</span><span>19</span><span>20</span><span>21</span><span>22</span><span>23</span><span>24</span><span>25</span><span>26</span><span>27</span><span>28</span><span>29</span><span>30</span><span>31</span></div></div>
      <div class="month"><p class="month-name">SEPTEMBER</p>
        <div class="weekdays"><span>S</span><span>M</span><span>T</span><span>W</span><span>T</span><span>F</span><span>S</span></div>
        <div class="days"><span>1</span><span>2</span><span>3</span><span>4</span><span>5</span><span>6</span><span>7</span><span>8</span><span>9</span><span>10</span><span>11</span><span>12</span><span>13</span><span>14</span><span>15</span><span>16</span><span>17</span><span>18</span><span>19</span><span>20</span><span>21</span><span>22</span><span>23</span><span>24</span><span>25</span><span>26</span><span>27</span><span>28</span><span>29</span><span>30</span></div></div>
      <div class="month"><p class="month-name">OCTOBER</p>
        <div class="weekdays"><span>S</span><span>M</span><span>T</span><span>W</span><span>T</span><span>F</span><span>S</span></div>
        <div class="days"><i></i><i></i><span>1</span><span>2</span><span>3</span><span>4</span><span>5</span><span>6</span><span>7</span><span>8</span><span>9</span><span>10</span><span>11</span><span>12</span><span>13</span><span>14</span><span>15</span><span>16</span><span>17</span><span>18</span><span>19</span><span>20</span><span>21</span><span>22</span><span>23</span><span>24</span><span>25</span><span>26</span><span>27</span><span>28</span><span>29</span><span>30</span><span>31</span></div></div>
      <div class="month"><p class="month-name">NOVEMBER</p>
        <div class="weekdays"><span>S</span><span>M</span><span>T</span><span>W</span><span>T</span><span>F</span><span>S</span></div>
        <div class="days"><i></i><i></i><i></i><i></i><i></i><span>1</span><span>2</span><span>3</span><span>4</span><span>5</span><span>6</span><span>7</span><span>8</span><span>9</span><span>10</span><span>11</span><span>12</span><span>13</span><span>14</span><span>15</span><span>16</span><span>17</span><span>18</span><span>19</span><span>20</span><span>21</span><span>22</span><span>23</span><span>24</span><span>25</span><span>26</span><span>27</span><span>28</span><span>29</span><span>30</span></div></div>
      <div class="month"><p class="month-name">DECEMBER</p>
        <div class="weekdays"><span>S</span><span>M</span><span>T</span><span>W</span><span>T</span><span>F</span><span>S</span></div>
        <div class="days"><span>1</span><span>2</span><span>3</span><span>4</span><span>5</span><span>6</span><span>7</span><span>8</span><span>9</span><span>10</span><span>11</span><span>12</span><span>13</span><span>14</span><span>15</span><span>16</span><span>17</span><span>18</span><span>19</span><span>20</span><span>21</span><span>22</span><span>23</span><span>24</span><span>25</span><span>26</span><span>27</span><span>28</span><span>29</span><span>30</span><span>31</span></div></div>
    </div>
  </section>

</div>
</body>
</html>
```